Four in One (Flexible infographic for Content Management Industry)

See attachment.
A graphic depicting 4 products, where each can stand on its own and each can be combined with others, but where, if all are taken together, the best result is achieved (the "super product").
Intended use is web. See attached file as an example.
The most basic idea is as the attached diagram shows, where 4 rectangles are arranged in a quadrangle, with a middle rectangle in the center representing the combined 4 products. This concept is fine except it is a bit too obvious as it stands. We are looking for either a variation of this or another concept.
The audience is technical + professional + enterprise - NOT consumers. Hence the design should be conservative in nature.
We are aware of tools like as Canva or Pictogram where such graphics are available, but we are looking for something with a bit more imagination and flexibility.
This graphic should be targeted to web sites and be delivered with vector-based (SVG) graphics.

```html
<!DOCTYPE html>
<html lang="en">
<head>
<meta charset="utf-8">
<title>Four in One – Super Product infographic</title>
<link href="https://fonts.googleapis.com/css2?family=Open+Sans:wght@400;600;700;800&display=swap" rel="stylesheet">
<style>
:root{
  --frame:#a9a9a9;
  --divider:#d8d8d8;
  --ink:#2e2e36;
  --outline-q1:#2f3d4d;
  --outline-q2:#3d7f8c;
  --outline-q3:#53628f;
  --outline-q4:#5e2f55;
  --outline-hub:#5a2b4c;
  --outline-q4-tab:#8a4f8d;
}
*{box-sizing:border-box;margin:0;padding:0}
html,body{width:1200px;height:328px;overflow:hidden;background:#fff}
body{font-family:"Open Sans",Arial,sans-serif;color:var(--ink);position:relative}
.shape-library{position:absolute;width:0;height:0;overflow:hidden}
.panel{position:absolute;top:0;width:400px;height:328px}
.panel-outline{left:0}
.panel-slate{left:400px;border-left:1px solid var(--divider)}
.panel-vivid{left:800px;border-left:1px solid var(--divider)}
.panel svg{position:absolute;left:0;top:0}
.hub{position:absolute;left:117px;top:150px;width:166px;height:32px;border-radius:16px;
  display:flex;align-items:center;justify-content:center;font-weight:800;font-size:19px;letter-spacing:-.3px;white-space:nowrap}
.panel-outline .hub{background:var(--outline-hub);color:#fff}
.panel-slate .hub,.panel-vivid .hub{background:#fff;color:#3a3a3a;border:1.5px solid var(--frame)}
.card{position:absolute;width:124px;text-align:center}
.card h3{font-size:8px;font-weight:700;margin-bottom:5px;white-space:nowrap;text-align:left;padding-left:2px}
.card p{font-size:4.8px;line-height:1.35;font-weight:600;margin-bottom:5px}
.card ul{list-style:none;display:inline-block;text-align:left;font-size:4.4px;font-weight:700;line-height:1.45}
.card li::before{content:"✔ "}
.card-tl{left:68px;top:80px}
.card-tr{left:210px;top:80px}
.card-bl{left:68px;top:196px}
.card-br{left:210px;top:196px}
.panel-slate .card,.panel-vivid .card{color:#fff}
</style>
</head>
<body>

<svg class="shape-library" aria-hidden="true">
  <defs>
    <path id="frame-tl" d="M61,17 H163 A41,41 0 0 1 204,58 V157 A10,10 0 0 1 194,167 H92 A41,41 0 0 1 51,126 V27 A10,10 0 0 1 61,17Z"/>
    <path id="frame-tr" d="M237,17 H339 A10,10 0 0 1 349,27 V126 A41,41 0 0 1 308,167 H206 A10,10 0 0 1 196,157 V58 A41,41 0 0 1 237,17Z"/>
    <path id="frame-bl" d="M92,161 H194 A10,10 0 0 1 204,171 V270 A41,41 0 0 1 163,311 H61 A10,10 0 0 1 51,301 V202 A41,41 0 0 1 92,161Z"/>
    <path id="frame-br" d="M206,161 H308 A41,41 0 0 1 349,202 V301 A10,10 0 0 1 339,311 H237 A41,41 0 0 1 196,270 V171 A10,10 0 0 1 206,161Z"/>
    <path id="leaf-tl" d="M64,24 H162 A34,34 0 0 1 196,58 V154 A6,6 0 0 1 190,160 H92 A34,34 0 0 1 58,126 V30 A6,6 0 0 1 64,24Z"/>
    <path id="leaf-tr" d="M238,24 H336 A6,6 0 0 1 342,30 V126 A34,34 0 0 1 308,160 H210 A6,6 0 0 1 204,154 V58 A34,34 0 0 1 238,24Z"/>
    <path id="leaf-bl" d="M92,168 H190 A6,6 0 0 1 196,174 V270 A34,34 0 0 1 162,304 H64 A6,6 0 0 1 58,298 V202 A34,34 0 0 1 92,168Z"/>
    <path id="leaf-br" d="M210,168 H308 A34,34 0 0 1 342,202 V298 A6,6 0 0 1 336,304 H238 A34,34 0 0 1 204,270 V174 A6,6 0 0 1 210,168Z"/>
    <g id="frame-set">
      <g fill="#fff" stroke="#a9a9a9" stroke-width="1.6">
        <use href="#frame-tl"/><use href="#frame-tr"/><use href="#frame-bl"/><use href="#frame-br"/>
      </g>
      <g fill="#fff">
        <use href="#frame-tl"/><use href="#frame-tr"/><use href="#frame-bl"/><use href="#frame-br"/>
      </g>
    </g>
    <g id="icon-set" fill="none" stroke-width="1.3">
      <path d="M82 38h8l4 4v11h-12z"/><path d="M85 45h6M85 48h6M85 51h6"/>
      <path d="M314 53l6 2.5v5c0 4-3 6.5-6 8-3-1.5-6-4-6-8v-5z"/><path d="M311 61l2 2 4-4"/>
      <path d="M82 269h8l4 4v11h-12z"/><path d="M85 276h6M85 279h6M85 282h6"/>
      <path d="M307 274a11 11 0 0 1 14 0M309.5 277.5a7 7 0 0 1 9 0"/>
    </g>
  </defs>
</svg>

<!-- Variant: outlined -->
<section class="panel panel-outline">
  <svg width="400" height="328" viewBox="0 0 400 328" aria-hidden="true">
    <use href="#frame-set"/>
    <use href="#leaf-tl" fill="#fff" stroke="var(--outline-q1)" stroke-width="1.6"/>
    <use href="#leaf-tr" fill="#fff" stroke="var(--outline-q2)" stroke-width="1.6"/>
    <use href="#leaf-bl" fill="#fff" stroke="var(--outline-q3)" stroke-width="1.6"/>
    <use href="#leaf-br" fill="#fff" stroke="var(--outline-q4)" stroke-width="1.6"/>
    <rect x="62" y="33" width="50" height="24" rx="2" fill="var(--outline-q1)"/>
    <rect x="290" y="49" width="48" height="24" rx="2" fill="var(--outline-q2)"/>
    <rect x="62" y="264" width="50" height="24" rx="2" fill="var(--outline-q3)"/>
    <rect x="252" y="264" width="86" height="24" rx="2" fill="var(--outline-q4-tab)"/>
    <use href="#icon-set" stroke="#fff" transform="translate(5 0)"/>
    <circle cx="319" cy="281.5" r="1.6" fill="#fff"/>
  </svg>
  <div class="hub">Super Product</div>
  <div class="card card-tl"><h3>Document Management</h3><p>Streamline document organization, access, and collaboration with easier file storage and sharing, leading to more efficient workflows .</p><ul><li>Centralized Document Control</li><li>Collaborative Workspace Integration</li><li>Automated Compliance Tracking</li><li>Check 4</li></ul></div>
  <div class="card card-tr"><h3>Security and Compliance</h3><p>Benefit from tailored cloud solutions, secure data storage, and expert disaster recovery planning for reliable and scalable IT operations.</p><ul><li>Custom Cloud Solutions</li><li>Secure Data Storage</li><li>Expert Disaster Recovery</li><li>Check 4</li></ul></div>
  <div class="card card-bl"><h3>Enterprise Resource Planning</h3><p>Simplify management across finance, sales, and operations, enabling better decision-making and improved productivity.</p><ul><li>Integrated Business Processes</li><li>Enhanced Decision-Making</li><li>Productivity Improvement</li><li>Check 4</li></ul></div>
  <div class="card card-br"><h3>Digital Transformation</h3><p>Turn scanned documents into easily searchable digital archives, boosting efficiency and accessibility.</p><ul><li>Instant searchable Archives with OCR</li><li>Automated Document Classification</li><li>DocuVault and Cloud Blob Ready</li><li>Check 4</li></ul></div>
</section>

<!-- Variant: slate fills -->
<section class="panel panel-slate">
  <svg width="400" height="328" viewBox="0 0 400 328" aria-hidden="true">
    <defs>
      <linearGradient id="slate-q1" x1="0" y1="0" x2="1" y2="1"><stop offset="0" stop-color="#2c3a4b"/><stop offset="1" stop-color="#4d5c72"/></linearGradient>
      <linearGradient id="slate-q2" x1="0" y1="0" x2="1" y2="1"><stop offset="0" stop-color="#3f8f9a"/><stop offset="1" stop-color="#5bb0b6"/></linearGradient>
      <linearGradient id="slate-q3" x1="0" y1="0" x2="1" y2="1"><stop offset="0" stop-color="#46557e"/><stop offset="1" stop-color="#5b6797"/></linearGradient>
      <linearGradient id="slate-q4" x1="0" y1="0" x2="1" y2="1"><stop offset="0" stop-color="#3a7f8c"/><stop offset="1" stop-color="#2b5f72"/></linearGradient>
    </defs>
    <use href="#frame-set"/>
    <use href="#leaf-tl" fill="url(#slate-q1)"/>
    <use href="#leaf-tr" fill="url(#slate-q2)"/>
    <use href="#leaf-bl" fill="url(#slate-q3)"/>
    <use href="#leaf-br" fill="url(#slate-q4)"/>
    <g fill="#fff">
      <rect x="62" y="33" width="50" height="24" rx="2"/>
      <rect x="290" y="49" width="48" height="24" rx="2"/>
      <rect x="62" y="264" width="50" height="24" rx="2"/>
      <rect x="290" y="264" width="48" height="24" rx="2"/>
    </g>
    <use href="#icon-set" stroke="#2e2e36"/>
    <circle cx="314" cy="281.5" r="1.6" fill="#2e2e36"/>
  </svg>
  <div class="hub">Super Product</div>
  <div class="card card-tl"><h3>Document Management</h3><p>Streamline document organization, access, and collaboration with easier file storage and sharing, leading to more efficient workflows .</p><ul><li>Centralized Document Control</li><li>Collaborative Workspace Integration</li><li>Automated Compliance Tracking</li><li>Check 4</li></ul></div>
  <div class="card card-tr"><h3>Security and Compliance</h3><p>Benefit from tailored cloud solutions, secure data storage, and expert disaster recovery planning for reliable and scalable IT operations.</p><ul><li>Custom Cloud Solutions</li><li>Secure Data Storage</li><li>Expert Disaster Recovery</li><li>Check 4</li></ul></div>
  <div class="card card-bl"><h3>Enterprise Resource Planning</h3><p>Simplify management across finance, sales, and operations, enabling better decision-making and improved productivity.</p><ul><li>Integrated Business Processes</li><li>Enhanced Decision-Making</li><li>Productivity Improvement</li><li>Check 4</li></ul></div>
  <div class="card card-br"><h3>Digital Transformation</h3><p>Turn scanned documents into easily searchable digital archives, boosting efficiency and accessibility.</p><ul><li>Instant searchable Archives with OCR</li><li>Automated Document Classification</li><li>DocuVault and Cloud Blob Ready</li><li>Check 4</li></ul></div>
</section>

<!-- Variant: vivid fills -->
<section class="panel panel-vivid">
  <svg width="400" height="328" viewBox="0 0 400 328" aria-hidden="true">
    <defs>
      <linearGradient id="vivid-q1" x1="0" y1="0" x2="1" y2="1"><stop offset="0" stop-color="#4b357c"/><stop offset="1" stop-color="#6a56a0"/></linearGradient>
      <linearGradient id="vivid-q2" x1="0" y1="0" x2="1" y2="1"><stop offset="0" stop-color="#c21a86"/><stop offset="1" stop-color="#8e1570"/></linearGradient>
      <linearGradient id="vivid-q3" x1="0" y1="0" x2="1" y2="1"><stop offset="0" stop-color="#2eb6c4"/><stop offset="1" stop-color="#2a8fb0"/></linearGradient>
      <linearGradient id="vivid-q4" x1="0" y1="0" x2="1" y2="1"><stop offset="0" stop-color="#1f78aa"/><stop offset="1" stop-color="#1b5a8e"/></linearGradient>
    </defs>
    <use href="#frame-set"/>
    <use href="#leaf-tl" fill="url(#vivid-q1)"/>
    <use href="#leaf-tr" fill="url(#vivid-q2)"/>
    <use href="#leaf-bl" fill="url(#vivid-q3)"/>
    <use href="#leaf-br" fill="url(#vivid-q4)"/>
    <g fill="#fff">
      <rect x="62" y="33" width="50" height="24" rx="2"/>
      <rect x="290" y="49" width="48" height="24" rx="2"/>
      <rect x="62" y="264" width="50" height="24" rx="2"/>
      <rect x="290" y="264" width="48" height="24" rx="2"/>
    </g>
    <use href="#icon-set" stroke="#111"/>
    <circle cx="314" cy="281.5" r="1.6" fill="#111"/>
  </svg>
  <div class="hub">Super Product</div>
  <div class="card card-tl"><h3>Document Management</h3><p>Streamline document organization, access, and collaboration with easier file storage and sharing, leading to more efficient workflows .</p><ul><li>Centralized Document Control</li><li>Collaborative Workspace Integration</li><li>Automated Compliance Tracking</li><li>Check 4</li></ul></div>
  <div class="card card-tr"><h3>Security and Compliance</h3><p>Benefit from tailored cloud solutions, secure data storage, and expert disaster recovery planning for reliable and scalable IT operations.</p><ul><li>Custom Cloud Solutions</li><li>Secure Data Storage</li><li>Expert Disaster Recovery</li><li>Check 4</li></ul></div>
  <div class="card card-bl"><h3>Enterprise Resource Planning</h3><p>Simplify management across finance, sales, and operations, enabling better decision-making and improved productivity.</p><ul><li>Integrated Business Processes</li><li>Enhanced Decision-Making</li><li>Productivity Improvement</li><li>Check 4</li></ul></div>
  <div class="card card-br"><h3>Digital Transformation</h3><p>Turn scanned documents into easily searchable digital archives, boosting efficiency and accessibility.</p><ul><li>Instant searchable Archives with OCR</li><li>Automated Document Classification</li><li>DocuVault and Cloud Blob Ready</li><li>Check 4</li></ul></div>
</section>

</body>
</html>
```